New flavour! New packaging for Velocity Energy Drink!

We need a new packaging designed to show off our new grape flavored energy drink! It will require box design with matching sachets!

Established in 2018 we are a fully Australian owned and operated business that started out with 2 gamers that got sick and tired of sugary energy drinks OR expensive powder from the USA.

We are an energy drink in the esports and gaming space. Our new product is an energy drink in powder in boxes of 30 sachets (please see attached for product example)

Please see example 1 and 2 for our competitors product. We would ideally like to go a bit more minimalist than them but still have a great color pop on black backing.

Target Market(s)

Gamer's and esports athletes between the ages or 18-30

Font styles to use
Sans Serif
Other font styles liked:
• Helvetica

Colors
886aae
ffffff

Requirements
Must have
• Black base/background.
• Vibrant purple N in the Velocity Logo.
• Same or slightly different shades of purple for some text and highlights.
• Black, white and some shades of a vibrant purple (for the grape flavor)
• ingredients list (may need to be reformatted to suit)
• Please see attached for legislative requirements on the box and sachets.
Nice to have
• minimalist design but enough to be eye catching and somewhat playful
• Twitter: @VLCT_FUEL
• Instagram: @VLCT_FUEL
• Facebook: @VLCTFUEL
Should not have
• OTHER COLORS.
• Overly complex designs.

```html
<!DOCTYPE html>
<html lang="en">
<head>
<meta charset="utf-8">
<title>Velocity Energy Drink – Grape Flavour Box</title>
<link rel="stylesheet" href="https://fonts.googleapis.com/css2?family=Exo+2:wght@800&family=Michroma&family=Ubuntu:wght@500;700&display=swap">
<style>
  :root {
    --page-bg: #9b9aa4;
    --box-top: #2e2e31;
    --box-bottom: #0b0b0d;
    --purple-deep: #5b2f92;
    --purple-vivid: #8e2c8e;
    --purple-text: #9a3aa6;
    --silver: #d2d3d6;
    --white: #f2f2f2;
    --grape-dark: #241a33;
    --grape-mid: #4d3a66;
  }
  * { margin: 0; padding: 0; box-sizing: border-box; }
  html, body { width: 852px; height: 1200px; overflow: hidden; }
  body { background: var(--page-bg); position: relative; }

  .box-front {
    position: absolute;
    left: 46px; top: 421px;
    width: 760px; height: 357px;
    background: linear-gradient(160deg, var(--box-top) 0%, var(--box-bottom) 70%);
    overflow: hidden;
  }
  .tagline {
    position: absolute; top: 30px; left: 0; width: 100%;
    text-align: center;
    font-family: "Michroma", sans-serif;
    font-size: 16px; font-variant: small-caps; letter-spacing: 1px;
    color: var(--purple-text);
  }
  .tagline .divider {
    display: inline-block; width: 2px; height: 24px;
    background: var(--purple-text); vertical-align: middle; margin: 0 12px;
  }
  .brand-name {
    position: absolute; left: 124px; top: 118px;
    font-family: "Exo 2", sans-serif; font-weight: 800;
    font-size: 66px; line-height: 1; letter-spacing: 2px;
    color: var(--silver);
  }
  .brand-sub {
    position: absolute; right: 197px; top: 188px;
    font-family: "Michroma", sans-serif; font-size: 12px; letter-spacing: 5px;
    color: var(--white);
  }
  .product-type {
    position: absolute; right: 197px; top: 212px;
    font-family: "Ubuntu", sans-serif; font-weight: 700; font-size: 25px;
    color: var(--white);
  }
  .accent-band {
    position: absolute; left: 0; top: 253px; width: 100%; height: 15px;
    background: linear-gradient(90deg, var(--purple-deep), var(--purple-vivid));
  }
  .flavour-tag {
    position: absolute; left: 356px; top: 245px; width: 207px; height: 33px;
    background: var(--box-bottom);
    border: 2px solid var(--purple-deep);
    border-top-color: transparent; border-bottom-color: transparent;
    text-align: center;
  }
  .flavour-tag::before, .flavour-tag::after {
    content: ""; position: absolute; width: 10px; height: 29px;
    border-top: 2px solid var(--purple-deep); border-bottom: 2px solid var(--purple-deep);
    top: 0;
  }
  .flavour-tag::before { left: -2px; }
  .flavour-tag::after { right: -2px; }
  .flavour-name {
    font-family: "Michroma", sans-serif; font-size: 14px; letter-spacing: 1px;
    color: var(--purple-text); line-height: 18px; display: block;
  }
  .flavour-extra {
    font-family: "Ubuntu", sans-serif; font-weight: 700; font-size: 9.5px;
    color: var(--purple-text); line-height: 12px; display: block;
  }
  .fruit-visual {
    position: absolute; left: 555px; top: 104px; width: 180px; height: 190px;
    border-radius: 50%;
    background: radial-gradient(circle at 55% 55%, var(--grape-mid) 0%, var(--grape-dark) 55%, transparent 72%);
  }
  .info-band {
    position: absolute; left: 0; bottom: 0; width: 100%; height: 45px;
    background: linear-gradient(90deg, #4a2770 0%, var(--purple-vivid) 100%);
    display: flex; align-items: center; justify-content: space-between;
    padding: 0 16px 0 33px;
    font-family: "Ubuntu", sans-serif; color: var(--silver);
  }
  .serves { font-weight: 700; font-size: 16px; letter-spacing: 0.5px; }
  .net-weight { font-weight: 500; font-size: 11.5px; }
</style>
</head>
<body>
  <section class="box-front">
    <p class="tagline">For gamers<span class="divider"></span>By gamers</p>
    <div class="fruit-visual" role="img" aria-label="Purple grapes with a water splash"></div>
    <h1 class="brand-name">VELOCITY</h1>
    <p class="brand-sub">ENERGY DRINK</p>
    <p class="product-type">ENERGY DRINK</p>
    <div class="accent-band"></div>
    <div class="flavour-tag">
      <span class="flavour-name">GRAPE FLAVOUR</span>
      <span class="flavour-extra">WITH GINSENG &amp; CAFFEINE</span>
    </div>
    <div class="info-band">
      <span class="serves">30 SERVES</span>
      <span class="net-weight">150 g (30 x 5 g)</span>
    </div>
  </section>
</body>
</html>
```